Business Card

I would like a business card with a picture of my husband and I that is unique and professional.

Industry/Entity Type

Business

Font styles to use
Serif

```html
<!DOCTYPE html>
<html lang="en">
<head>
<meta charset="utf-8">
<title>Vale Leadership Group – Business Card</title>
<link href="https://fonts.googleapis.com/css2?family=Cinzel:wght@500;700&family=Jost:wght@400;700&display=swap" rel="stylesheet">
<style>
  :root {
    --page: #2a2a2a;
    --card-black: #0b0b0b;
    --card-panel: #161616;
    --gold: #d9a93a;
    --gold-light: #f2cf6e;
    --gold-dark: #9c7420;
    --pattern-a: #1c1c1e;
    --pattern-b: #0e0e0f;
    --photo-a: #e9e6e2;
    --photo-b: #8a8580;
  }
  html, body {
    margin: 0;
    width: 1200px;
    height: 1023px;
    overflow: hidden;
    background: var(--page);
  }
  .canvas {
    position: relative;
    width: 1200px;
    height: 1023px;
  }
  .card {
    position: absolute;
    width: 700px;
    height: 400px;
    border-radius: 6px;
    overflow: hidden;
    box-shadow: 0 14px 40px rgba(0,0,0,.55);
  }
  .card-front {
    left: 60px;
    top: 60px;
    background: var(--card-black);
  }
  .card-back {
    left: 440px;
    top: 563px;
    background: var(--pattern-b);
  }
  .front-band {
    position: absolute;
    inset: 0;
  }
  .portrait {
    position: absolute;
    left: 355px;
    top: 28px;
    width: 160px;
    height: 125px;
    border: 6px solid var(--gold);
    background: linear-gradient(150deg, var(--photo-a) 0%, var(--photo-a) 45%, var(--photo-b) 100%);
  }
  .contact {
    position: absolute;
    left: 245px;
    top: 180px;
    color: var(--gold);
    font-family: "Jost", sans-serif;
  }
  .contact-name {
    margin: 0;
    font-weight: 700;
    font-size: 30px;
    letter-spacing: .3px;
  }
  .contact-title {
    margin: 4px 0 0;
    font-size: 17px;
    line-height: 1.1;
  }
  .contact-line {
    margin: 10px 0 0;
    font-size: 17px;
  }
  .contact-line + .contact-line { margin-top: 4px; }
  .brand-front {
    position: absolute;
    left: 40px;
    top: 250px;
    width: 190px;
    text-align: center;
    color: var(--gold);
    font-family: "Cinzel", serif;
  }
  .brand-mark {
    display: flex;
    align-items: center;
    justify-content: center;
    gap: 10px;
    font-weight: 700;
    font-size: 34px;
  }
  .brand-square {
    width: 14px;
    height: 14px;
    background: var(--gold);
  }
  .brand-rule {
    height: 1px;
    background: var(--gold);
    margin: 14px 0 6px;
  }
  .brand-caption {
    font-size: 11px;
    font-weight: 500;
    letter-spacing: .5px;
  }
  .back-pattern {
    position: absolute;
    inset: 0;
    background: radial-gradient(ellipse at 45% 45%, var(--pattern-a) 0%, var(--pattern-b) 80%);
  }
  .brand-back {
    position: absolute;
    left: 0;
    right: 0;
    top: 130px;
    text-align: center;
    color: var(--gold);
    font-family: "Cinzel", serif;
  }
  .brand-back .brand-mark { font-size: 64px; gap: 16px; }
  .brand-back .brand-square { width: 22px; height: 22px; }
  .brand-back .brand-rule {
    width: 360px;
    margin: 22px auto 10px;
  }
  .brand-back .brand-caption { font-size: 20px; letter-spacing: 1.5px; }
</style>
</head>
<body>
<main class="canvas">

  <section class="card card-front">
    <svg class="front-band" width="700" height="400" viewBox="0 0 700 400" aria-hidden="true">
      <defs>
        <linearGradient id="goldSweep" x1="0" y1="0" x2="0" y2="1">
          <stop offset="0" stop-color="#f2cf6e"/>
          <stop offset=".5" stop-color="#d9a93a"/>
          <stop offset="1" stop-color="#9c7420"/>
        </linearGradient>
      </defs>
      <path d="M560 0 Q575 230 430 400 L700 400 L700 0 Z" fill="#161616"/>
      <path d="M548 0 Q562 232 418 400 L434 400 Q580 230 566 0 Z" fill="url(#goldSweep)"/>
      <path d="M620 0 Q632 210 540 400 L546 400 Q640 210 628 0 Z" fill="url(#goldSweep)" opacity=".8"/>
    </svg>

    <div class="portrait" role="img" aria-label="Portrait photo of the couple"></div>

    <div class="contact">
      <h1 class="contact-name">Renata Vale</h1>
      <p class="contact-title">Professional Mentorship<br>Strategist</p>
      <p class="contact-line">555-014-2286</p>
      <p class="contact-line">RenataVale@example.com</p>
    </div>

    <div class="brand-front">
      <div class="brand-mark"><span class="brand-square"></span>Vale</div>
      <div class="brand-rule"></div>
      <div class="brand-caption">VALE LEADERSHIP GROUP</div>
    </div>
  </section>

  <section class="card card-back">
    <div class="back-pattern" role="img" aria-label="Faint repeating crest pattern background"></div>
    <div class="brand-back">
      <div class="brand-mark"><span class="brand-square"></span>Vale</div>
      <div class="brand-rule"></div>
      <div class="brand-caption">VALE LEADERSHIP GROUP</div>
    </div>
  </section>

</main>
</body>
</html>
```